Professional looking Roller Blind Discount Card that portrays quality at a value for money price!

We need a double sided business card designed as a discount card. Size 90mm wide x 55mm high.We would like it to look professional and portray quality at a value for money price point.I have uploaded a word document with a basic layout with the information we want included on each side of the card. Please put your own thought into the layout.

As per word document attached.

```html
<!DOCTYPE html>
<html lang="en">
<head>
<meta charset="UTF-8">
<title>Roller Blinds Discount Card</title>
<link rel="stylesheet" href="https://fonts.googleapis.com/css2?family=Arimo:wght@400;700&family=Open+Sans:wght@400;600;700;800&display=swap">
<style>
  :root {
    --bg: #2a2a2c;
    --card: #ffffff;
    --aqua: #0fa3cc;
    --aqua-soft: #8fd3e8;
    --aqua-pale: #dff3f9;
    --ink: #111111;
    --grey: #6b6b6b;
    --cloud-line: #5a3a22;
    --photo-a: #6d7f63;
    --photo-b: #3f5a3a;
    --photo-c: #9a8d86;
  }
  * { box-sizing: border-box; margin: 0; padding: 0; }
  html, body {
    width: 1200px; height: 900px; overflow: hidden;
    background: var(--bg);
    font-family: "Open Sans", Arial, sans-serif;
    color: var(--ink);
  }
  .canvas { position: relative; width: 1200px; height: 900px; }

  .card {
    position: absolute;
    width: 640px; height: 391px;
    background: var(--card);
    overflow: hidden;
    box-shadow: 0 14px 30px rgba(0,0,0,.55);
  }
  .card--front { left: 80px; top: 48px; }
  .card--back { left: 480px; top: 470px; }

  .card__wash {
    position: absolute; inset: 0;
    background: linear-gradient(150deg, rgba(255,255,255,0) 42%, var(--aqua-pale) 62%, var(--aqua-soft) 100%);
  }
  .card--front .card__wash {
    background: linear-gradient(200deg, rgba(255,255,255,0) 40%, var(--aqua-pale) 60%, var(--aqua-soft) 100%);
  }

  /* Front */
  .front__title {
    position: absolute; left: 160px; top: 26px;
    font-family: "Arimo", Arial, sans-serif; font-weight: 700; font-size: 34px;
  }
  .front__subtitle {
    position: absolute; left: 60px; top: 76px;
    font-family: "Arimo", Arial, sans-serif; font-size: 22px;
  }
  .front__photo {
    position: absolute; left: 60px; top: 118px; width: 330px; height: 200px;
    border: 6px solid var(--aqua);
    background: linear-gradient(135deg, var(--photo-c) 0%, var(--photo-a) 35%, var(--photo-b) 70%, var(--photo-c) 100%);
  }
  .front__cloud { position: absolute; left: 410px; top: 18px; width: 210px; height: 140px; }
  .front__cloud-text {
    position: absolute; left: 440px; top: 48px; width: 150px;
    text-align: center; font-weight: 700; font-size: 15px; line-height: 1.25;
  }
  .front__call {
    position: absolute; left: 60px; bottom: 28px;
    font-family: "Arimo", Arial, sans-serif; font-size: 28px;
  }
  .front__call strong { font-weight: 700; }

  .brand {
    position: absolute; display: flex; align-items: center; gap: 8px;
    font-family: "Open Sans", Arial, sans-serif; font-weight: 600; color: var(--aqua);
    white-space: nowrap;
  }
  .brand__mark { width: 14px; height: 14px; background: var(--aqua); }
  .card--front .brand { left: 430px; top: 210px; font-size: 20px; }
  .card--back .brand { right: 22px; top: 262px; font-size: 17px; }

  /* Back */
  .back__offer {
    position: absolute; left: 0; right: 0; top: 30px; text-align: center;
    font-weight: 800; font-size: 58px; line-height: 1;
  }
  .back__band {
    position: absolute; left: 0; right: 0; top: 98px; height: 78px;
    background: var(--aqua); color: #fff; text-align: center;
    font-weight: 600; font-size: 20px; line-height: 1.3; padding-top: 10px;
  }
  .back__features {
    position: absolute; left: 16px; right: 200px; top: 196px;
    display: flex;
  }
  .feature { flex: 1; text-align: center; padding: 0 6px; }
  .feature + .feature { border-left: 3px solid var(--grey); }
  .feature__head { font-weight: 800; font-size: 22px; white-space: nowrap; }
  .feature__text { font-weight: 700; font-size: 14px; line-height: 1.25; margin-top: 6px; }
  .back__call {
    position: absolute; left: 0; right: 0; bottom: 26px; text-align: center;
    font-family: "Arimo", Arial, sans-serif; font-size: 30px;
  }
  .back__call strong { font-weight: 700; }
</style>
</head>
<body>
<main class="canvas">

  <section class="card card--front" aria-label="Card front">
    <div class="card__wash"></div>
    <h1 class="front__title">Roller Blinds</h1>
    <p class="front__subtitle">FREE in Home Measure &amp; Quote</p>
    <div class="front__photo" role="img" aria-label="Photo of a room with roller blinds over windows looking onto a garden"></div>
    <svg class="front__cloud" viewBox="0 0 210 140" aria-hidden="true">
      <path d="M40 95 C10 95 8 60 32 55 C25 25 65 15 80 30 C90 8 130 8 140 28 C160 12 195 28 185 55 C205 65 198 100 170 98 C160 118 120 118 110 104 C95 120 55 118 40 95 Z"
            fill="#fff" stroke="var(--cloud-line)" stroke-width="3"/>
      <circle cx="160" cy="122" r="5" fill="#fff" stroke="var(--cloud-line)" stroke-width="2"/>
      <circle cx="176" cy="133" r="3.5" fill="#fff" stroke="var(--cloud-line)" stroke-width="2"/>
    </svg>
    <p class="front__cloud-text">Huge<br>Selection<br>of<br>Fabrics</p>
    <div class="brand"><span class="brand__mark"></span>Kestrel Blinds Co</div>
    <p class="front__call">Call <strong>0491570156</strong> Today</p>
  </section>

  <section class="card card--back" aria-label="Card back">
    <div class="card__wash"></div>
    <p class="back__offer">25% OFF</p>
    <div class="back__band">
      Quality Custom Made Roller Blinds<br>Blockout - Screen - Light&nbsp; Filtering
    </div>
    <div class="back__features">
      <div class="feature">
        <p class="feature__head">FREE</p>
        <p class="feature__text">in<br>Home Measure<br>and Quote</p>
      </div>
      <div class="feature">
        <p class="feature__head">BEST PRICE</p>
        <p class="feature__text">Best Price<br>Guarentee</p>
      </div>
      <div class="feature">
        <p class="feature__head">FAMILY</p>
        <p class="feature__text">Family Owned<br>and Operated</p>
      </div>
    </div>
    <div class="brand"><span class="brand__mark"></span>Kestrel Blinds Co</div>
    <p class="back__call">Call <strong>0491570156</strong> Today</p>
  </section>

</main>
</body>
</html>
```